New shirt company looking for a fun and edgy online retail website design

We're a new company looking for a simple yet attractive website to sell shirts/tops to a mostly younger female audience. Our name is Tilvo Shirt Co. and the ArtPavilion logo is uploaded. We're thinking a home page, three separate pages for our shirt "collections", and a contact page/cart page for a grand total of 5 pages. We'd like the website to be coded, easy for the consumer to navigate/shop/checkout, and easy to link to various social media platforms and online websites. For colors, we're aiming for various blues, light grey, and maybe tan/khaki. Our goal is to launch with approximately 20-30 tops/shirts (or 7-10) per page. Please let us know if you have any questions and thank you for helping us! We are very excited to see what is created!

Target Market(s)

Female teens to early twenties

Coding

Coded - Design and coding required

Number of Pages Required

3 page

Font styles to use
Decorative
Script

Colors
cee9f5
85cae6
33a6d7
0393ce
cfdfed
85acd3

Requirements
Must have
• Online shopping/purchasing capabilities, dropdowns to select sizes for each item, easy to add/remove new or seasoned items.

```html
<!DOCTYPE html>
<html lang="en">
<head>
<meta charset="utf-8">
<title>Tilvo Shirt Co. – Home</title>
<link href="https://fonts.googleapis.com/css2?family=Montserrat:wght@400;500;600;700&display=swap" rel="stylesheet">
<style>
:root{
  --sky:#cee9f5; --powder:#85cae6; --azure:#33a6d7; --brand:#0393ce;
  --mist:#cfdfed; --steel:#85acd3; --ink:#2b2b2b; --text:#444;
  --footer:#222; --footer-deep:#161616; --tile:#333;
}
*{margin:0;padding:0;box-sizing:border-box}
html,body{width:1200px;height:4622px;overflow:hidden}
body{position:relative;font-family:'Montserrat',sans-serif;color:var(--text);background:#fff}
.abs{position:absolute}
.btn{position:absolute;background:var(--brand);color:#fff;font-size:13px;font-weight:600;display:flex;align-items:center;justify-content:center;text-transform:uppercase}
.section-title{position:absolute;left:0;width:1200px;text-align:center;color:var(--azure);font-size:31px;font-weight:700;text-transform:uppercase}
.photo{position:absolute}

/* header */
.logo-box{left:63px;top:0;width:206px;height:102px;background:var(--powder);display:flex;align-items:center;justify-content:center;color:#1b4f8a;font-weight:700;font-size:20px}
.nav{left:517px;top:42px;display:flex;gap:42px;font-size:15px;color:#333}
.nav .active{color:var(--brand)}
.round-icon{width:40px;height:40px;border-radius:50%;background:var(--brand);top:33px}

/* hero */
.hero-kicker{left:230px;top:262px;color:var(--brand);font-size:20px}
.hero-title{left:230px;top:302px;font-size:32px;line-height:38px;color:#333;font-weight:500}
.badge{left:658px;top:185px;width:86px;height:86px;border-radius:50%;background:var(--brand);border:4px solid #fff;color:#fff;font-size:20px;text-align:center;display:flex;align-items:center;justify-content:center;line-height:24px}
.dot{width:12px;height:12px;border-radius:50%;background:#999}
.dot.on{background:var(--brand)}

/* bands */
.band-sky{left:0;top:574px;width:1200px;height:793px;background:var(--sky)}
.band-mist{left:0;top:1367px;width:1200px;height:547px;background:var(--mist)}

.about-title{left:592px;top:645px;font-size:31px;font-weight:700;color:var(--azure)}
.about-copy{left:592px;top:696px;width:540px;font-size:16px;line-height:27.5px;color:#333}

.collection-label{position:absolute;top:1498px;width:300px;text-align:center;font-size:20px;font-weight:600;color:#333}

.card{position:absolute;width:280px;height:450px;background:#fff}
.card .photo{left:0;top:0;width:280px;height:248px}
.card h3{position:absolute;top:262px;left:0;width:280px;text-align:center;font-size:19px;font-weight:600;line-height:27px;color:#222}
.card .price{position:absolute;top:332px;left:0;width:280px;text-align:center;font-size:19px;color:var(--brand)}
.card .price s{font-weight:700}
.card .price b{font-weight:700;margin:0 10px}
.card .btn{left:75px;top:373px;width:129px;height:54px}

.banner{left:0;top:2998px;width:1200px;height:386px;background:linear-gradient(90deg,#3e3f44 0%,#5a5148 45%,#6a7c84 75%,#5d7d88 100%)}
.banner-text{left:0;top:3120px;width:1200px;text-align:center;color:#fff;font-size:32px;font-weight:600;line-height:39px}
.banner-text span{color:var(--azure)}
.social{width:46px;height:46px;border-radius:50%;background:var(--brand);top:3237px}

.quote{left:390px;top:3545px;width:420px;text-align:center;font-size:15px;line-height:27.5px;color:#444}
.quote-by{left:0;top:3683px;width:1200px;text-align:center;color:var(--brand);font-size:20px}

.tile{position:absolute;top:3843px;width:153px;height:115px;background:var(--steel);color:#fff;font-size:30px;line-height:37px;padding:22px 0 0 12px;text-transform:uppercase}

.footer{left:0;top:4049px;width:1200px;height:451px;background:var(--footer)}
.footer-base{left:0;top:4500px;width:1200px;height:122px;background:var(--footer-deep)}
.up{left:568px;top:4018px;width:62px;height:62px;border-radius:50%;background:var(--brand)}
.f-logo{left:233px;top:4162px;width:146px;height:81px;background:var(--powder);display:flex;align-items:center;justify-content:center;color:#1b4f8a;font-weight:700;font-size:15px}
.contact-row{position:absolute;left:168px;display:flex;align-items:center;gap:16px;color:#fff;font-size:27px;font-weight:500}
.contact-row .ring{width:56px;height:56px;border-radius:50%;border:2px solid #fff;display:flex;align-items:center;justify-content:center}
.f-head{top:4148px;color:#fff;font-size:25px;text-transform:uppercase}
.f-link{position:absolute;width:204px;height:42px;background:#333;color:#fff;font-size:15px;display:flex;align-items:center;padding-left:24px;text-transform:uppercase}
.copyright{left:63px;top:4559px;color:#fff;font-size:15px}
.pay{position:absolute;top:4550px;width:65px;height:38px;border-radius:3px;background:#e8e8e8;color:#333;font-size:11px;font-weight:600;display:flex;align-items:center;justify-content:center}
</style>
</head>
<body>

<!-- header -->
<div class="abs logo-box">Tilvo Shirt Co.</div>
<nav class="abs nav"><span class="active">HOME</span><span>ABOUT US</span><span>COLLECTIONS</span><span>CONTACT US</span></nav>
<div class="abs round-icon" style="left:1030px"><svg width="40" height="40" viewBox="0 0 40 40"><path d="M11 13h3l3 11h10l2-8H16" fill="none" stroke="#fff" stroke-width="2.2"/><circle cx="18" cy="28" r="1.8" fill="#fff"/><circle cx="26" cy="28" r="1.8" fill="#fff"/></svg></div>
<div class="abs round-icon" style="left:1096px"><svg width="40" height="40" viewBox="0 0 40 40"><circle cx="20" cy="16" r="5" fill="#fff"/><path d="M11 28c1-5 5-7 9-7s8 2 9 7z" fill="#fff"/></svg></div>

<!-- hero -->
<svg class="abs" style="left:74px;top:278px" width="24" height="38" viewBox="0 0 24 38"><path d="M20 3L5 19l15 16" fill="none" stroke="var(--brand)" stroke-width="5"/></svg>
<svg class="abs" style="left:1106px;top:278px" width="24" height="38" viewBox="0 0 24 38"><path d="M4 3l15 16L4 35" fill="none" stroke="var(--brand)" stroke-width="5"/></svg>
<div class="abs hero-kicker">TILVO SHIRT CO.</div>
<div class="abs hero-title">THE ULTIMATE CLOTHING,<br>TO SEE THE WORLD IN.</div>
<div class="btn" style="left:230px;top:400px;width:242px;height:54px">Explore Colections</div>
<div class="abs" style="left:693px;top:214px;width:222px;height:206px;border:4px solid var(--brand);border-radius:6px"></div>
<div class="photo" role="img" aria-label="Young woman in denim jacket and mustard top wearing sunglasses" style="left:720px;top:240px;width:290px;height:334px;background:linear-gradient(180deg,#f2f2f2 0%,#6f8eb3 40%,#e3a63a 70%,#5d7aa5 100%)"></div>
<div class="abs badge">30%<br>OFF</div>
<div class="abs dot on" style="left:569px;top:535px"></div>
<div class="abs dot" style="left:594px;top:535px"></div>
<div class="abs dot" style="left:619px;top:535px"></div>

<!-- about -->
<div class="abs band-sky"></div>
<div class="abs band-mist"></div>
<div class="photo" role="img" aria-label="Folded jeans, white knitwear and glasses" style="left:66px;top:655px;width:388px;height:388px;border-radius:50%;border:3px solid #fff;background:radial-gradient(circle at 45% 55%,#f4f4f4 0%,#d8dde3 50%,#4b5d7a 100%)"></div>
<div class="photo" role="img" aria-label="Rack of shirts on hangers" style="left:329px;top:867px;width:186px;height:186px;border-radius:50%;border:5px solid #fff;background:linear-gradient(90deg,#6e6e6e,#a9a9a9,#555,#8c8c8c)"></div>
<div class="abs about-title">ABOUT US</div>
<p class="abs about-copy">Ac ut consequat semper viverra nam libero justo laoreet sit. Mi tempus imperdiet nulla malesuada pellentesque elit eget gravida. Mauris in aliquam sem fringilla ut morbi tincidunt. Egestas sed sed risus pretium. Porttitor leo a diam sollicitudin tempor id. Venenatis urna cursus eget nunc scelerisque viverra. Sollicitudin nibh sit amet commodo nulla facilisi nullam. Viverra suspendisse potenti nullam ac tortor vitae. Tellus id interdum velit laoreet. Volutpat odio facilisis mauris sit amet massa vitae. Nullam eget felis eget nunc. Hendrerit gravida rutrum quisque non tellus orci ac auctor augue.</p>
<div class="btn" style="left:592px;top:1001px;width:174px;height:54px">Products</div>

<!-- collections -->
<div class="section-title" style="top:1149px">COLLECTION’S</div>
<div class="photo" role="img" aria-label="Woman in beige top in the countryside" style="left:155px;top:1271px;width:178px;height:178px;transform:rotate(45deg);border-radius:34px;border:3px solid #fff;background:linear-gradient(180deg,#9aa7a2,#c9c4b4,#6f6a5c)"></div>
<div class="photo" role="img" aria-label="Woman in denim jacket sitting against a striped wall" style="left:510px;top:1271px;width:178px;height:178px;transform:rotate(45deg);border-radius:34px;border:3px solid #fff;background:linear-gradient(180deg,#e5e8ec,#56657a,#1f2329)"></div>
<div class="photo" role="img" aria-label="Smiling woman in denim shirt" style="left:889px;top:1271px;width:178px;height:178px;transform:rotate(45deg);border-radius:34px;border:3px solid #fff;background:linear-gradient(180deg,#f4f4f4,#b8866a,#4f7bb3)"></div>
<div class="collection-label" style="left:94px">WINTERS SPECIALE</div>
<div class="collection-label" style="left:449px">COLLECTION NAME</div>
<div class="collection-label" style="left:828px">NAME OF COLLECTION</div>
<div class="btn" style="left:180px;top:1545px;width:129px;height:54px">Explore</div>
<div class="btn" style="left:535px;top:1545px;width:129px;height:54px">Explore</div>
<div class="btn" style="left:890px;top:1545px;width:129px;height:54px">Explore</div>

<!-- products -->
<div class="section-title" style="top:1709px">PRODUCTS</div>
<div class="card" style="left:65px;top:1780px"><div class="photo" role="img" aria-label="Black lace-sleeve top" style="background:linear-gradient(180deg,#fafafa,#222 35%,#1a1a1a 85%,#fafafa)"></div><h3>Tilvo’s net sleeves<br>black top #344453</h3><div class="price"><s>$30</s><b>$25</b>30%off</div><div class="btn">Know More</div></div>
<div class="card" style="left:461px;top:1780px"><div class="photo" role="img" aria-label="Beige off-shoulder sweater" style="background:linear-gradient(180deg,#fafafa,#cbbfb2 35%,#b9ad9f 80%,#556 95%)"></div><h3>Tilvo’s net sleeves<br>black top #344453</h3><div class="price"><s>$30</s><b>$25</b>30%off</div><div class="btn">Know More</div></div>
<div class="card" style="left:856px;top:1780px"><div class="photo" role="img" aria-label="White wrap blouse" style="background:linear-gradient(180deg,#fafafa,#e9ecef 40%,#dfe3e8 85%,#333)"></div><h3>Tilvo’s net sleeves<br>black top #344453</h3><div class="price"><s>$30</s><b>$25</b>30%off</div><div class="btn">Know More</div></div>
<div class="card" style="left:65px;top:2338px"><div class="photo" role="img" aria-label="Grey cold-shoulder top" style="background:linear-gradient(180deg,#fafafa,#6b7378 35%,#5e666b 90%)"></div><h3>Tilvo’s net sleeves<br>black top #344453</h3><div class="price"><s>$30</s><b>$25</b>30%off</div><div class="btn">Know More</div></div>
<div class="card" style="left:461px;top:2338px"><div class="photo" role="img" aria-label="Taupe cold-shoulder top" style="background:linear-gradient(180deg,#fafafa,#c9bdb1 35%,#bcb0a4 90%)"></div><h3>Tilvo’s net sleeves<br>black top #344453</h3><div class="price"><s>$30</s><b>$25</b>30%off</div><div class="btn">Know More</div></div>
<div class="card" style="left:856px;top:2338px"><div class="photo" role="img" aria-label="Beige off-shoulder sweater" style="background:linear-gradient(180deg,#fafafa,#cbbfb2 35%,#b9ad9f 80%,#556 95%)"></div><h3>Tilvo’s net sleeves<br>black top #344453</h3><div class="price"><s>$30</s><b>$25</b>30%off</div><div class="btn">Know More</div></div>
<div class="btn" style="left:479px;top:2872px;width:242px;height:54px">Explore More</div>

<!-- banner -->
<div class="abs banner" role="img" aria-label="Clothing rack of colourful shirts beside a smiling woman in a yellow shirt"></div>
<div class="abs banner-text">OUR PROUDCTS ARE MADE<br>TO OFFER <span>COMFORT|</span></div>
<div class="abs social" style="left:463px" aria-label="Social link one"></div>
<div class="abs social" style="left:544px" aria-label="Social link two"></div>
<div class="abs social" style="left:623px" aria-label="Social link three"></div>
<div class="abs social" style="left:702px" aria-label="Social link four"></div>

<!-- testimonials -->
<div class="section-title" style="top:3442px">TESTIMONIALS</div>
<svg class="abs" style="left:26px;top:3584px" width="24" height="38" viewBox="0 0 24 38"><path d="M20 3L5 19l15 16" fill="none" stroke="var(--brand)" stroke-width="5"/></svg>
<svg class="abs" style="left:1150px;top:3584px" width="24" height="38" viewBox="0 0 24 38"><path d="M4 3l15 16L4 35" fill="none" stroke="var(--brand)" stroke-width="5"/></svg>
<p class="abs quote">Lorem ipsum dolor sit amet, consectetur adipiscing elit, sed do eiusmod tempor incididunt ut labore et dolore magna aliqua. Quis ipsum suspendisse ultrices gravida. Risus commodo viverra maecenas</p>
<div class="abs quote-by">-Mara Lind</div>
<div class="abs dot on" style="left:569px;top:3748px"></div>
<div class="abs dot" style="left:594px;top:3748px"></div>
<div class="abs dot" style="left:619px;top:3748px"></div>

<div class="tile" style="left:95px">Casual<br>Shirts</div>
<div class="tile" style="left:310px">High<br>Neck</div>
<div class="tile" style="left:524px">Loose<br>Top</div>
<div class="tile" style="left:739px">V-<br>Necks</div>
<div class="tile" style="left:953px">Round<br>Neck</div>

<!-- footer -->
<div class="abs footer"></div>
<div class="abs footer-base"></div>
<div class="abs up"><svg width="62" height="62" viewBox="0 0 62 62"><path d="M20 36l11-11 11 11" fill="none" stroke="#fff" stroke-width="4"/></svg></div>
<div class="abs f-logo">Tilvo Shirt Co.</div>
<div class="contact-row" style="top:4285px"><span class="ring"><svg width="26" height="26" viewBox="0 0 24 24"><path d="M6.6 10.8a15 15 0 006.6 6.6l2.2-2.2c.3-.3.7-.4 1-.2 1.1.4 2.3.6 3.6.6.6 0 1 .4 1 1V20c0 .6-.4 1-1 1A17 17 0 013 4c0-.6.4-1 1-1h3.5c.6 0 1 .4 1 1 0 1.3.2 2.5.6 3.6.1.3 0 .7-.2 1z" fill="#fff"/></svg></span>5550 2147 3090</div>
<div class="contact-row" style="top:4378px;left:112px"><span class="ring"><svg width="24" height="24" viewBox="0 0 24 24"><rect x="3" y="6" width="18" height="12" rx="1.5" fill="#fff"/><path d="M3.5 6.5l8.5 6.5 8.5-6.5" fill="none" stroke="#222" stroke-width="1.6"/></svg></span>hello@tilvoshirt.com</div>
<div class="abs f-head" style="left:588px">Explore</div>
<div class="abs f-head" style="left:884px">Sitemap</div>
<div class="f-link" style="left:592px;top:4194px">Winter Speciale</div>
<div class="f-link" style="left:592px;top:4262px">Collection Name</div>
<div class="f-link" style="left:592px;top:4330px">The Collections</div>
<div class="f-link" style="left:592px;top:4398px">My Cart</div>
<div class="f-link" style="left:884px;top:4194px">Home</div>
<div class="f-link" style="left:884px;top:4262px">Collections</div>
<div class="f-link" style="left:884px;top:4330px">Products</div>
<div class="f-link" style="left:884px;top:4398px">Contact Us</div>
<div class="abs copyright">© Copyright Tilvo Clothings  pvt ltd</div>
<div class="pay" style="left:709px">Cardo</div>
<div class="pay" style="left:799px">Sendly</div>
<div class="pay" style="left:889px">Amberpay</div>
<div class="pay" style="left:979px">Orbis</div>
<div class="pay" style="left:1069px">Paynook</div>

</body>
</html>
```